Copperline Structural Roof Inc.

We need a business card design for a commercial roofing company metro Boston based. We are a roofing company that help people manage buildings and build relationships with clients. We would like a unique card that stands out. We want a business card with a white background. We do not want a roof as the logo.

Industry/Entity Type

Roofing

```html
<!DOCTYPE html>
<html lang="en">
<head>
<meta charset="utf-8">
<title>Copperline Structural Roof Inc. — Business Card</title>
<link rel="stylesheet" href="https://fonts.googleapis.com/css2?family=Arimo:wght@400&family=Barlow:wght@400;600&display=swap">
<style>
  :root {
    --backdrop: #e9e7e3;
    --card: #fbfaf7;
    --brand-blue: #1a6fc2;
    --accent-blue: #2aa0dc;
    --icon-blue: #1f8fd6;
    --text-grey: #5b5b5b;
  }
  * { box-sizing: border-box; margin: 0; padding: 0; }
  html, body {
    width: 1200px; height: 800px; overflow: hidden;
    background: var(--backdrop);
  }
  .canvas {
    width: 1200px; height: 800px;
    display: flex; align-items: center; justify-content: center;
  }
  .business-card {
    position: relative;
    width: 840px; height: 480px;
    background: var(--card);
    box-shadow: 0 10px 30px rgba(0,0,0,0.12);
  }
  .wordmark {
    position: absolute; left: 80px; top: 200px; width: 300px;
    font-family: "Barlow", sans-serif; font-weight: 600;
    font-size: 34px; line-height: 1.1; color: var(--brand-blue);
  }
  .contact-block {
    position: absolute; left: 440px; top: 110px;
  }
  .person-name {
    font-family: "Barlow", sans-serif; font-weight: 400;
    font-size: 28px; color: var(--brand-blue); line-height: 1.15;
  }
  .person-role {
    font-family: "Barlow", sans-serif; font-weight: 400;
    font-size: 19px; color: var(--accent-blue); margin-bottom: 34px;
  }
  .contact-list { list-style: none; }
  .contact-item {
    display: flex; align-items: flex-start; gap: 12px;
    font-family: "Arimo", sans-serif; font-size: 18px;
    color: var(--text-grey); line-height: 1.3; margin-bottom: 22px;
  }
  .contact-icon { width: 18px; height: 18px; flex: none; margin-top: 2px; fill: var(--icon-blue); }
</style>
</head>
<body>
<main class="canvas">
  <section class="business-card">
    <div class="wordmark">Copperline Structural Roof Inc.</div>

    <div class="contact-block">
      <h1 class="person-name">Dana Whitcombe</h1>
      <p class="person-role">Founder</p>
      <ul class="contact-list">
        <li class="contact-item">
          <svg class="contact-icon" viewBox="0 0 18 18" aria-hidden="true"><path d="M2 17V4h7v13zM10 17V8h6v9zM3.5 6h1.5v1.5H3.5zM6 6h1.5v1.5H6zM3.5 9h1.5v1.5H3.5zM6 9h1.5v1.5H6z" fill-rule="evenodd"/></svg>
          <span>240 Harbor Line Drive, Suite 8<br>Quincy, MA 02169<br>617/555-0142</span>
        </li>
        <li class="contact-item">
          <svg class="contact-icon" viewBox="0 0 18 18" aria-hidden="true"><path d="M4 2l3 3-1.6 2.2a10 10 0 0 0 5.4 5.4L13 11l3 3-2 2.5C7.5 16 2 10.5 1.5 4z"/></svg>
          <span>617/555-0178</span>
        </li>
        <li class="contact-item">
          <svg class="contact-icon" viewBox="0 0 18 18" aria-hidden="true"><path d="M1 4h16v10H1zM2 5l7 5 7-5" stroke="#fbfaf7" stroke-width="1"/></svg>
          <span>dwhitcombe@copperlineroof.com</span>
        </li>
        <li class="contact-item">
          <svg class="contact-icon" viewBox="0 0 18 18" aria-hidden="true"><path d="M5 1h8v4H5zM2 6h14v7h-3v4H5v-4H2zM6 11h6v5H6z"/></svg>
          <span>617/555-0193</span>
        </li>
      </ul>
    </div>
  </section>
</main>
</body>
</html>
```